Simple elegant business card

General card for a fin and television director.
Just want name, email, phone and address.

Target Market(s)

Prospective employers

Industry/Entity Type

Business

Requirements
Must have
• As above
Nice to have
• Logo but not necessary.
Should not have
• Not too colourful or funky.
• Simplicity and elegance the way to go.

```html
<!DOCTYPE html>
<html lang="en">
<head>
<meta charset="utf-8">
<title>Lena Marsh — Business Card</title>
<link rel="stylesheet" href="https://fonts.googleapis.com/css2?family=Mulish:wght@400;800&display=swap">
<style>
  :root {
    --backdrop: #1c1c1e;
    --card-light: #ecece9;
    --card-dark: #1f2124;
    --ink-dark: #2a2a2c;
    --ink-mid: #8a8a8a;
    --ink-soft: #a9a9a6;
    --ink-light: #f2f2f2;
    --ink-muted-dark: #5a5c60;
  }
  * { margin: 0; padding: 0; box-sizing: border-box; }
  html, body {
    width: 1200px;
    height: 900px;
    overflow: hidden;
    background: var(--backdrop);
    font-family: "Mulish", sans-serif;
  }
  .canvas {
    position: relative;
    width: 1200px;
    height: 900px;
  }
  .card {
    position: absolute;
    width: 640px;
    height: 350px;
    padding: 52px 56px;
    display: flex;
    flex-direction: column;
    justify-content: space-between;
    box-shadow: 0 18px 40px rgba(0, 0, 0, 0.45);
  }
  .card--light {
    left: 80px;
    top: 100px;
    background: var(--card-light);
  }
  .card--dark {
    left: 480px;
    top: 470px;
    background: var(--card-dark);
  }
  .card__name {
    font-weight: 800;
    font-size: 30px;
    letter-spacing: 0.04em;
    text-transform: uppercase;
    line-height: 1;
  }
  .card--light .card__name { color: var(--ink-dark); }
  .card--dark .card__name { color: var(--ink-light); }
  .card__contact {
    font-weight: 400;
    font-size: 15px;
    line-height: 1.35;
  }
  .card--light .card__line--primary { color: var(--ink-dark); }
  .card--light .card__line--address { color: var(--ink-soft); }
  .card--dark .card__line--primary { color: var(--ink-light); }
  .card--dark .card__line--address { color: var(--ink-muted-dark); }
</style>
</head>
<body>
<main class="canvas">
  <section class="card card--light" aria-label="Business card, light side">
    <h1 class="card__name">Lena Marsh</h1>
    <address class="card__contact" style="font-style:normal">
      <p class="card__line card__line--primary">+ 1 310 555 0148 / lenamarsh@mail.com</p>
      <p class="card__line card__line--address">218 Harbor Lane, Santa Monica, 90405 CA USA</p>
    </address>
  </section>

  <section class="card card--dark" aria-label="Business card, dark side">
    <h2 class="card__name">Lena Marsh</h2>
    <address class="card__contact" style="font-style:normal">
      <p class="card__line card__line--primary">+ 1 310 555 0148 / lenamarsh@mail.com</p>
      <p class="card__line card__line--address">218 Harbor Lane, Santa Monica, 90405 CA USA</p>
    </address>
  </section>
</main>
</body>
</html>
```